High Quality Business card for Property Management Agency - Super Classy and professional design

High Quality Business card design.

We need a business card designed for our Property Management Agency.
We are located on Sydney's Northern Beaches and manage beautiful properties along the beach and harbor.
We need a design that oozes modern, classy and professional.
I would like it to be double sided with contact details and logo on the front and just the logo on the back.

I need a print ready PDF version of the file as well as an editable photoshop (PSD) version of the file.

Logo and information details attached.

Target Market(s)

Property owners/investors, Male and Female Aged 28-65

Industry/Entity Type

Real Estate

Contact Information for Business Card

Tom Carrick
Tel: 0467 239 018
Email: tom@harvestlaneestates.com.au
Website: www.harvestlaneestates.com.au
Address: Level 2, 17 Wattlecourt Rd, Dunmarra NSW 2187

Font styles to use
Sans Serif

Requirements
Must have
• - Logo front and back
• - Business card details listed above and attached
• - Colour
Nice to have
• Sleek and professional

```html
<!DOCTYPE html>
<html lang="en">
<head>
<meta charset="utf-8">
<title>Harvest Lane Estates – Business Card</title>
<link rel="stylesheet" href="https://fonts.googleapis.com/css2?family=Open+Sans:wght@400;700&display=swap">
<style>
  :root {
    --page-bg: #e7e4df;
    --card-white: #ffffff;
    --card-dark: #2b2b2c;
    --ink: #1a1a1a;
    --teal: #2a9aa3;
    --text-body: #2e2e2e;
    --logo-light: #ffffff;
  }
  * { box-sizing: border-box; margin: 0; padding: 0; }
  html, body {
    width: 1200px; height: 900px; overflow: hidden;
    background: var(--page-bg);
    font-family: "Open Sans", Arial, sans-serif;
  }
  .canvas { position: relative; width: 1200px; height: 900px; }
  .card {
    position: absolute; left: 267px; width: 666px; height: 380px;
    overflow: hidden;
    box-shadow: 0 6px 18px rgba(0,0,0,.18);
  }
  .card--back { top: 40px; background: var(--card-dark); }
  .card--front { top: 480px; background: var(--card-white); }

  .card__shapes { position: absolute; inset: 0; }

  .wordmark {
    position: absolute; display: flex; align-items: center; gap: 12px;
    font-weight: 700; letter-spacing: 1px; text-transform: uppercase;
    white-space: nowrap;
  }
  .wordmark__mark { width: 22px; height: 22px; background: var(--teal); flex: none; }
  .card--back .wordmark {
    left: 50%; top: 50%; transform: translate(-50%, -50%);
    font-size: 38px; color: var(--logo-light);
  }
  .card--front .wordmark {
    left: 326px; top: 152px; font-size: 24px; gap: 10px; color: var(--ink);
  }
  .card--front .wordmark__mark { width: 16px; height: 16px; }

  .agent-name {
    position: absolute; left: 92px; top: 22px;
    font-size: 21px; font-weight: 700; color: var(--teal);
  }
  .contact {
    position: absolute; left: 36px; top: 112px;
    font-size: 15px; line-height: 22px; color: var(--text-body);
    list-style: none;
  }
  .contact__address { margin-bottom: 10px; }
  .contact__row { display: flex; align-items: center; gap: 10px; }
  .contact__icon { width: 13px; height: 13px; flex: none; fill: var(--teal); }
</style>
</head>
<body>
<main class="canvas">

  <section class="card card--back" aria-label="Card back">
    <div class="wordmark">
      <span class="wordmark__mark"></span>
      <span class="wordmark__name">Harvest Lane Estates</span>
    </div>
  </section>

  <section class="card card--front" aria-label="Card front">
    <svg class="card__shapes" width="666" height="380" viewBox="0 0 666 380">
      <polygon points="0,0 26,0 0,30" fill="var(--teal)"/>
      <polygon points="36,0 76,0 66,48 0,48 0,44" fill="var(--ink)"/>
      <polygon points="0,240 300,306 296,322 0,266" fill="var(--teal)"/>
      <polygon points="312,318 666,318 666,380 298,380" fill="var(--ink)"/>
    </svg>

    <h1 class="agent-name">Tom Carrick</h1>

    <ul class="contact">
      <li class="contact__address">Level 2, 17 Wattlecourt Rd,<br>Dunmarra NSW 2187</li>
      <li class="contact__row">
        <svg class="contact__icon" viewBox="0 0 16 16"><path d="M3.5 1l3 3-1.8 1.8a9 9 0 0 0 5.5 5.5L12 9.5l3 3-2 2C6.5 14 2 9.5 1.5 3z"/></svg>
        <span>0467 239 018</span>
      </li>
      <li class="contact__row">
        <svg class="contact__icon" viewBox="0 0 16 16"><path d="M1 3h14v10H1z M1 3l7 6 7-6" fill="none" stroke="var(--teal)" stroke-width="1.6"/></svg>
        <span>tom@harvestlaneestates.com.au</span>
      </li>
      <li class="contact__row">
        <svg class="contact__icon" viewBox="0 0 16 16"><circle cx="8" cy="8" r="7"/></svg>
        <span>www.harvestlaneestates.com.au</span>
      </li>
    </ul>

    <div class="wordmark">
      <span class="wordmark__mark"></span>
      <span class="wordmark__name">Harvest Lane Estates</span>
    </div>
  </section>

</main>
</body>
</html>
```